Kestrel Building Works Business Card and more!

We need a business card design for Kestrel Building Works Ltd, a respected building company that specialises in high quality designer homes.

We're after a sleek, clean, modern business card that incorporates our new logo (see attached) and colours, with black being the background.

We are Certified Trade Craftsmen and need to include their logo (see attached) on our cards, balancing but not taking over our logo.

Details to be included:

Warren Pike
Director

Phone: 0219462513
Email: kestrelbuild.nz@mailbox-example.nz
Website: www.kestrelbuildingworks.co.nz

Additional Information

A start up website is also under construction and needing attention and letterheads are needed!

We look forward to your designs!

Target Market(s)

30+ people who are interested in building new or renovating current homes

Industry/Entity Type

Construction

Contact Information for Business Card

Warren Pike
Director

Phone: 0219462513
Facebook: www.socialpage-example.com/kestrelbuild.nz

Font styles to use
Serif

Colors

Designer to choose colors to be used in the design.

Requirements
Must have
• Our new logo
• Our colours
• ctc logo

```html
<!DOCTYPE html>
<html lang="en">
<head>
<meta charset="utf-8">
<title>Kestrel Building Works – Business Card</title>
<link href="https://fonts.googleapis.com/css2?family=EB+Garamond:wght@400;600&family=Cinzel:wght@400;600&display=swap" rel="stylesheet">
<style>
  :root {
    --backdrop: #3a2c24;
    --card: #272727;
    --card-edge: #1c1c1c;
    --gold: #c9a06a;
    --silver: #d9d9d9;
    --muted: #8a8a8a;
    --ink-light: #f1f1f1;
  }
  * { margin: 0; padding: 0; box-sizing: border-box; }
  html, body {
    width: 1200px; height: 715px; overflow: hidden;
    background: var(--backdrop);
  }
  .canvas {
    position: relative; width: 1200px; height: 715px;
    display: flex; align-items: center; justify-content: center; gap: 40px;
  }
  .card {
    position: relative; width: 540px; height: 310px;
    background: var(--card);
    box-shadow: 0 8px 22px rgba(0,0,0,.45);
    border: 1px solid var(--card-edge);
  }
  .brand {
    position: absolute; text-align: center;
    font-family: "Cinzel", serif; font-weight: 600;
  }
  .brand-name {
    display: block; font-size: 34px; letter-spacing: 6px; line-height: 1;
  }
  .brand-sub {
    display: block; font-size: 14px; letter-spacing: 4.5px; margin-top: 8px;
  }
  .card-back .brand { left: 0; right: 0; top: 105px; color: var(--silver); }
  .card-back .website {
    position: absolute; left: 0; right: 0; top: 215px; text-align: center;
    font-family: "EB Garamond", serif; font-size: 13px; color: var(--muted);
  }
  .card-front .brand { right: 40px; top: 85px; color: var(--gold); }
  .brand-mark {
    display: inline-block; width: 10px; height: 10px; border-radius: 50%;
    background: currentColor; margin-left: 8px; vertical-align: middle;
  }
  .contact {
    position: absolute; left: 36px; top: 160px;
    font-family: "EB Garamond", serif; color: var(--ink-light);
  }
  .person-name { font-size: 17px; font-weight: 600; color: var(--gold); }
  .person-role { font-size: 11px; color: var(--ink-light); margin-bottom: 14px; }
  .contact-line {
    display: flex; align-items: center; gap: 9px;
    font-size: 12.5px; line-height: 20px;
  }
  .contact-line svg { width: 11px; height: 11px; flex: none; }
  .badge {
    position: absolute; right: 28px; bottom: 24px;
    width: 62px; height: 62px; border-radius: 50%;
    background: var(--ink-light);
    border: 4px solid var(--card);
    box-shadow: 0 0 0 2px var(--ink-light);
  }
</style>
</head>
<body>
<main class="canvas">
  <section class="card card-back">
    <div class="brand">
      <span class="brand-name">KESTREL</span>
      <span class="brand-sub">BUILDING WORKS</span>
    </div>
    <p class="website">www.kestrelbuildingworks.co.nz</p>
  </section>

  <section class="card card-front">
    <div class="brand">
      <span class="brand-name">KESTREL<span class="brand-mark"></span></span>
      <span class="brand-sub">BUILDING WORKS</span>
    </div>
    <div class="contact">
      <p class="person-name">Warren Pike</p>
      <p class="person-role">Director</p>
      <p class="contact-line">
        <svg viewBox="0 0 12 12" aria-hidden="true"><path d="M2 1h2.5l1 3-1.5 1a7 7 0 0 0 3 3l1-1.5 3 1V11A9 9 0 0 1 1 2z" fill="#f1f1f1"/></svg>
        0219462513
      </p>
      <p class="contact-line">
        <svg viewBox="0 0 12 12" aria-hidden="true"><rect x="1" y="2.5" width="10" height="7" fill="none" stroke="#f1f1f1"/><path d="M1 2.5l5 4 5-4" fill="none" stroke="#f1f1f1"/></svg>
        kestrelbuild.nz@mailbox-example.nz
      </p>
      <p class="contact-line">
        <svg viewBox="0 0 12 12" aria-hidden="true"><circle cx="6" cy="6" r="4" fill="#f1f1f1"/></svg>
        socialpage-example.com/kestrelbuild
      </p>
    </div>
    <div class="badge" role="img" aria-label="Certified trade craftsmen badge"></div>
  </section>
</main>
</body>
</html>
```